Business card design needed

Business Card design required for new small plumbing business.
Would like a logo/text look that is simple and unique and does not have to be representative of a plumbing company (ie. having a cartoon plumber or toilet etc) as the companyname is self explanatory.
Would like the main colour to be green (lime green).
Updates

Industry/Entity Type

Plumber

Contact Information for Business Card

BRAVELL PLUMBING
ABN 61 904 127 558 003

Trevor Hasketh
Licensed Plumber 83615
Phone: 0412 870 245

27 Bravell Drive,
Fernbrook. 3999 Northvale

Email: bravellplumbing@mailnest.example

Logo Text

Bravell Plumbing

Logo styles of interest
Character Logo
Wordmark Logo
Lettermark Logo

```html
<!DOCTYPE html>
<html lang="en">
<head>
<meta charset="utf-8">
<title>Bravell Plumbing – Business Card</title>
<link rel="stylesheet" href="https://fonts.googleapis.com/css2?family=Roboto:wght@400;500;700&family=Roboto+Condensed:wght@400;700&display=swap">
<style>
  :root {
    --lime: #a3d11c;
    --lime-light: #c9e95a;
    --lime-pale: #e4f5a8;
    --ink: #5b7a10;
    --ink-dark: #4a6508;
    --paper: #ffffff;
    --backdrop: #eeeeea;
  }
  * { box-sizing: border-box; margin: 0; padding: 0; }
  html, body { width: 1200px; height: 871px; overflow: hidden; }
  body { background: var(--backdrop); position: relative; font-family: "Roboto", Arial, sans-serif; }

  .card {
    position: absolute; left: 120px; top: 50px;
    width: 840px; height: 513px;
    background: var(--lime);
    overflow: hidden;
    box-shadow: 0 10px 30px rgba(0,0,0,.18);
  }
  .card__waves { position: absolute; inset: 0; }

  .brand {
    position: absolute; right: 60px; top: 40px;
    display: flex; flex-direction: column; align-items: flex-end;
  }
  .brand__mark { width: 60px; height: 60px; background: var(--lime); margin-bottom: 12px; margin-right: 50px; }
  .brand__name {
    font-family: "Roboto Condensed", Arial, sans-serif; font-weight: 700;
    font-size: 30px; color: var(--lime); line-height: 1;
  }
  .brand__abn {
    font-family: "Roboto Condensed", Arial, sans-serif; font-weight: 400;
    font-size: 18px; color: var(--ink); margin-top: 3px;
  }

  .holder { position: absolute; right: 60px; top: 200px; text-align: right; }
  .holder__name { font-weight: 700; font-size: 44px; color: var(--ink); line-height: 1.05; }
  .holder__role { font-weight: 400; font-size: 22px; color: var(--ink-dark); margin-top: 6px; }

  .address {
    position: absolute; left: 44px; bottom: 34px;
    font-weight: 500; font-size: 22px; line-height: 1.3; color: var(--ink);
    font-style: normal;
  }
  .address__email { font-size: 19px; }
  .phone {
    position: absolute; right: 50px; bottom: 110px;
    font-size: 30px; font-weight: 400; color: var(--ink);
  }

  .lockup {
    position: absolute; left: 728px; top: 610px; width: 420px;
    display: flex; flex-direction: column; align-items: center;
  }
  .lockup__mark { width: 140px; height: 140px; background: var(--lime); margin-bottom: 12px; }
  .lockup__name {
    font-family: "Roboto Condensed", Arial, sans-serif; font-weight: 700;
    font-size: 46px; color: var(--lime); line-height: 1.05;
  }
  .lockup__abn {
    font-family: "Roboto Condensed", Arial, sans-serif; font-weight: 400;
    font-size: 32px; color: var(--ink); line-height: 1.1;
  }
</style>
</head>
<body>
  <section class="card">
    <svg class="card__waves" viewBox="0 0 840 513" width="840" height="513" aria-hidden="true">
      <ellipse cx="540" cy="170" rx="520" ry="300" fill="var(--lime-light)"/>
      <ellipse cx="550" cy="150" rx="470" ry="262" fill="var(--lime)"/>
      <ellipse cx="560" cy="140" rx="430" ry="236" fill="var(--lime-pale)"/>
      <ellipse cx="570" cy="130" rx="400" ry="214" fill="var(--lime-light)"/>
      <ellipse cx="580" cy="120" rx="378" ry="200" fill="var(--paper)"/>
    </svg>

    <div class="brand">
      <span class="brand__mark"></span>
      <span class="brand__name">BRAVELL PLUMBING</span>
      <span class="brand__abn">ABN 61 904 127 558 003</span>
    </div>

    <div class="holder">
      <h1 class="holder__name">Trevor Hasketh</h1>
      <p class="holder__role">Licensed Plumber 83615</p>
    </div>

    <address class="address">
      27 Bravell Drive<br>
      Fernbrook<br>
      3999 Northvale<br>
      <span class="address__email">bravellplumbing@mailnest.example</span>
    </address>

    <p class="phone">Ph: 0412 870 245</p>
  </section>

  <div class="lockup">
    <span class="lockup__mark"></span>
    <span class="lockup__name">BRAVELL PLUMBING</span>
    <span class="lockup__abn">ABN 61 904 127 558 003</span>
  </div>
</body>
</html>
```